Webdesign für Hunde- und Katzenernährungsberatung
Zielgruppe
Hunde und Katzenernährungsberatung, für Menschen, die auch bei ihren Hunden und Katzen auf gesunde, natürliche Ernährung achten wollen, ohne unnötigen Geschmacksverstärker, Zucker, Zusatzstoffe, etc. die gesundheitliche Probleme bei den Tieren verursachen können.
Umstellung auf natürliche, artgerechte Fütterung, teils roh, teils gekocht, angepasst auf Grösse, Rasse, Alter etc., auch speziell für Welpen
Beratung bei:
Übergewicht
Allergien
Unverträglichkeiten
Magen-Darm Problemen
individuelle Ernährungspläne
Selbsthergestellte Kekse, Leckerlies, Snacks, Pralinen und div. Hausmannskost in Einmachgläsern (alles auf Vorbestellung).
Diverse Accessoires
Halsbänder, Leinen, Geschirr aus div. natürlichen Materialien
Lern- und Spielzeug aus Holz und Stoff
div. Zubehör für Tiere, sowie auch für Frauchen und Herrchen
Aufgabenstellung
Die Seite sollte stilvoll aber nicht überfüllt sein und im Retro/Vintage Stil gehalten werden, da das Logo bereits sehr wirksam und eher auffällig ist, dezente Töne im Hintergrund, die Nahrungsmittel werden dann ev. auf Schieferplatten oder unauffälligem Hintergrund platziert. Ich sollte zu einem späteren Zeitpunkt selber Fotos, Links, Texte, etc. einfach dazu fügen können.

```html
<!DOCTYPE html>
<html lang="de">
<head>
<meta charset="utf-8">
<title>Napfglück – Ernährungsberatung für Hund und Katze</title>
<link href="https://fonts.googleapis.com/css2?family=Kaushan+Script&family=Montserrat:wght@400;600;700&family=Open+Sans:wght@400;600&display=swap" rel="stylesheet">
<style>
:root{
  --stage:#e4e4e4;
  --blue:#9bc5dd;
  --blue-deep:#79a5c1;
  --blue-btn:#6f9bb8;
  --orange:#cf7c1f;
  --text:#5a5a5a;
  --paper:#ffffff;
  --paper-soft:#f4f4f4;
  --line:#cfd6db;
}
*{box-sizing:border-box;margin:0;padding:0}
html,body{width:1200px;height:3000px;overflow:hidden}
body{background:radial-gradient(ellipse at 50% 40%,#f6f6f6 0%,var(--stage) 70%);font-family:"Montserrat",sans-serif;color:var(--text);position:relative}
.page{position:absolute;left:396px;top:0;width:408px;height:3000px;background:var(--paper);overflow:hidden}
.abs{position:absolute}
.script{font-family:"Kaushan Script",cursive;font-weight:400}
.body-text{font-size:6.2px;line-height:10.8px;color:var(--text)}
.btn{position:absolute;display:flex;align-items:center;justify-content:center;color:#fff;font-size:6px;font-weight:700;letter-spacing:.2px;text-transform:uppercase}
.btn-blue{background:var(--blue-btn)}
.btn-orange{background:var(--orange)}
.caps-list{list-style:none;font-size:7.4px;line-height:13px;color:#444;text-transform:uppercase}
.media{position:absolute}

.site-header{left:0;top:0;width:408px;height:47px;background:#fff;border-top:3px solid var(--blue)}
.brand{position:absolute;left:24px;top:6px;width:88px;height:78px;border-radius:50%;background:#fff;display:flex;flex-direction:column;align-items:center;justify-content:center;z-index:3}
.brand-name{font-family:"Montserrat",sans-serif;font-weight:700;font-size:12px;color:var(--blue-deep)}
.brand-dot{width:30px;height:30px;border-radius:50%;background:var(--blue);margin-bottom:4px}
.menu-icon{position:absolute;right:16px;top:21px;width:22px}
.menu-icon span{display:block;height:1.5px;background:var(--blue);margin-bottom:2.5px}

.hero{left:0;top:47px;width:408px;height:442px;background:var(--blue)}
.hero-rule{position:absolute;left:76px;width:258px;height:2px;background:#fff;border-radius:2px}
.hero-title{position:absolute;left:0;width:408px;top:55px;text-align:center;font-size:40px;line-height:38px;color:#6b3d15}
.hero-title .light{color:#fff}
.hero-sub{position:absolute;left:0;width:408px;top:141px;text-align:center;font-size:7.4px;color:#333}
.hero-edge{position:absolute;left:0;bottom:0;width:408px;height:7px;background:#f0a24a}

.h-orange{color:var(--orange);font-size:22px;line-height:25px}
.h-white{color:#fff;font-size:20px;line-height:24px}

.wave-top{position:absolute;left:0;width:408px;height:8px;background:radial-gradient(circle at 50% 100%,var(--blue) 5px,transparent 5.6px) 0 0/14px 8px repeat-x}
.wave-bottom{position:absolute;left:0;width:408px;height:8px;background:radial-gradient(circle at 50% 0,var(--blue) 5px,transparent 5.6px) 0 0/14px 8px repeat-x}

.tick-list{list-style:none;font-size:6px;line-height:13.4px;font-weight:700;color:#fff;text-transform:uppercase}
.tick-list li{display:flex;align-items:center;gap:5px}
.tick-list svg{width:9px;height:7px}
.orange-list{list-style:none;font-size:6px;line-height:11px;font-weight:700;color:var(--orange);text-transform:uppercase}

.shop{left:0;top:1835px;width:408px;height:565px;background:radial-gradient(circle at 50% 45%,#b3d4e7 0%,var(--blue) 60%)}
.shop-title{position:absolute;left:0;width:408px;top:18px;text-align:center;color:#fff;font-size:22px}
.shop-tabs{position:absolute;left:0;width:408px;top:57px;text-align:center;font-size:5.8px;font-weight:700;color:#fff;letter-spacing:.2px}
.card{position:absolute;width:116px;height:193px;background:#fff;box-shadow:0 1px 3px rgba(0,0,0,.15)}
.card-img{position:absolute;left:14px;top:8px;width:88px;height:62px;background:linear-gradient(180deg,#b56a36 0%,#93502a 100%)}
.card-name{position:absolute;left:0;width:116px;top:80px;text-align:center;font-size:5.6px;font-weight:700;color:var(--orange)}
.card-desc{position:absolute;left:7px;width:102px;top:91px;text-align:center;font-size:5px;line-height:7.6px;color:#666}
.card-rule{position:absolute;left:8px;width:100px;top:128px;border-top:1px dotted #c9c9c9}
.card-price{position:absolute;left:0;width:116px;top:131px;text-align:center;font-size:20px;font-weight:600;color:var(--orange);line-height:22px}
.card-tax{position:absolute;left:0;width:116px;top:155px;text-align:center;font-size:4.8px;line-height:7px;color:#666}
.card-tax b{color:var(--orange);font-weight:600}
.card .btn{left:8px;width:100px;top:177px;height:14px;font-size:5.8px}

.newsletter{left:0;top:2400px;width:408px;height:97px;background:var(--blue-deep);font-family:"Open Sans",sans-serif;color:#fff}
.news-title{position:absolute;left:0;width:408px;top:17px;text-align:center;font-size:15.5px;font-weight:400}
.news-sub{position:absolute;left:0;width:408px;top:36px;text-align:center;font-size:8px;color:#e8f1f7}
.news-input{position:absolute;left:16px;top:55px;width:279px;height:21px;background:#fff;font-size:7px;color:#aaa;padding:6px 12px}
.news-btn{position:absolute;left:301px;top:55px;width:91px;height:21px;background:#fff;color:var(--blue-deep);font-size:7.4px;font-weight:600;display:flex;align-items:center;justify-content:center}

.site-footer{left:0;top:2497px;width:408px;height:471px;background:var(--paper-soft)}
.footer-brand{position:absolute;left:104px;top:18px;width:200px;height:110px;display:flex;flex-direction:column;align-items:center}
.footer-brand .brand-name{font-size:17px;margin-bottom:6px}
.footer-brand .brand-dot{width:84px;height:84px;margin:0;background:#fff;border:3px solid var(--blue)}
.address{position:absolute;left:0;width:408px;top:152px;text-align:center;font-size:5.8px;line-height:12.5px;color:#555}
.address .web{color:var(--orange);font-weight:600}
.social{position:absolute;left:128px;top:196px;display:flex;gap:21px}
.social span{width:14px;height:14px;border-radius:50%;background:var(--blue-deep)}
.contact-title{position:absolute;left:0;width:408px;top:232px;text-align:center;color:var(--orange);font-size:26px}
.contact-sub{position:absolute;left:0;width:408px;top:268px;text-align:center;font-size:6.4px;color:#555}
.field{position:absolute;border-bottom:1px solid var(--line);font-size:5.8px;color:#888;padding-bottom:5px;text-transform:uppercase}
.field.active{color:var(--orange);border-bottom-color:#e2b27a}
.copy-check{position:absolute;left:16px;top:433px;font-size:6px;color:#555;display:flex;align-items:center;gap:5px}
.copy-check i{width:6px;height:6px;background:#9aa4aa;display:block}
.bottom-bar{left:0;top:2968px;width:408px;height:32px;background:var(--blue-deep);color:#fff;font-size:5.6px}
.bottom-bar .left{position:absolute;left:16px;top:13px}
.bottom-bar .right{position:absolute;right:16px;top:13px;font-weight:600}
</style>
</head>
<body>
<div class="page">

  <header class="abs site-header">
    <div class="brand"><span class="brand-dot"></span><span class="brand-name">Napfglück</span></div>
    <div class="menu-icon"><span></span><span></span><span></span></div>
  </header>

  <section class="abs hero">
    <div class="media" role="img" aria-label="Illustration: Katze und Hund sitzen nebeneinander" style="left:60px;top:210px;width:348px;height:225px;background:linear-gradient(180deg,#a9cde2 0%,#c4b49a 100%)"></div>
    <div class="hero-rule" style="top:49px"></div>
    <h1 class="hero-title script">Lorem ipsum<br><span class="light">dolor sit amet</span></h1>
    <p class="hero-sub">LOREM IPSUM DOLOR SIT AMET CONSECTETUR ADIPISCING ELIT</p>
    <div class="hero-rule" style="top:158px;left:64px;width:282px"></div>
    <div class="btn btn-blue" style="left:150px;top:180px;width:104px;height:18px;font-size:6.6px">Online Shop</div>
    <div class="hero-edge"></div>
  </section>

  <section>
    <div class="media" role="img" aria-label="Portraitfoto der Ernährungsberaterin" style="left:0;top:505px;width:198px;height:305px;background:linear-gradient(180deg,#f0eeec 0%,#d8cdc2 100%)"></div>
    <h2 class="abs script h-orange" style="left:211px;top:524px;width:190px">Willkommen auf<br>unserer Website</h2>
    <p class="abs body-text" style="left:211px;top:581px;width:184px">Lorem ipsum dolor sit amet, consectetur adipiscing elit, sed do eiusmod tempor incididunt ut labore et dolore magna aliqua. Ut enim ad minim veniam, quis nostrud exercitation ullamco laboris nisi ut aliquip ex ea commodo consequat. Duis aute irure dolor in reprehenderit in voluptate velit esse cillum dolore eu fugiat nulla pariatur.</p>
    <h3 class="abs script h-orange" style="left:211px;top:651px;font-size:18px">Beratung bei:</h3>
    <ul class="abs caps-list" style="left:211px;top:681px">
      <li>Übergewicht <span style="color:var(--orange)">|</span> Allergien</li>
      <li>Unverträglichkeiten</li>
      <li>Magen-Darm Problemen</li>
      <li>Individuelle Ernährungspläne</li>
    </ul>
    <p class="abs body-text" style="left:211px;top:740px;width:184px">Lorem ipsum dolor sit amet, consectetur adipiscing elit, sed do eiusmod tempor incididunt ut labore et dolore magna aliqua. Ut enim ad minim veniam, quis nostrud exercitation ullamco laboris nisi ut aliquip ex ea commodo consequat.</p>
  </section>

  <section>
    <div class="media" role="img" aria-label="Foto: Hund frisst aus einem Metallnapf" style="left:200px;top:870px;width:208px;height:266px;background:linear-gradient(180deg,#ffffff 0%,#eadfd3 100%)"></div>
    <div class="media" role="img" aria-label="Foto: Katze frisst aus einem Metallnapf" style="left:0;top:1010px;width:200px;height:126px;background:linear-gradient(180deg,#ffffff 0%,#e6e2de 100%)"></div>
    <h2 class="abs script h-orange" style="left:15px;top:830px">Ernährungsberatung</h2>
    <p class="abs body-text" style="left:15px;top:871px;width:280px">Lorem ipsum dolor sit amet, consectetur adipiscing elit, sed do eiusmod tempor incididunt ut labore et dolore magna aliqua. Ut enim ad minim veniam, quis nostrud exercitation ullamco laboris nisi ut aliquip ex ea commodo consequat. Duis aute irure dolor in reprehenderit in voluptate velit esse cillum dolore eu fugiat nulla pariatur.</p>
    <p class="abs body-text" style="left:15px;top:926px;width:250px">Lorem ipsum dolor sit amet, consectetur adipiscing elit, sed do eiusmod tempor incididunt ut labore et dolore magna aliqua.</p>
    <div class="btn btn-orange" style="left:15px;top:964px;width:84px;height:16px">Mehr Infos</div>
  </section>

  <section>
    <div class="abs" style="left:0;top:1177px;width:408px;height:303px;background:radial-gradient(circle at 25% 55%,#c9e1ef 0%,var(--blue) 55%)"></div>
    <div class="wave-top" style="top:1169px"></div>
    <div class="wave-bottom" style="top:1480px"></div>
    <div class="media" role="img" aria-label="Foto: kleiner Hund mit Napf im Maul und Hundekekse" style="left:0;top:1177px;width:200px;height:340px;background:linear-gradient(180deg,#d9c3a6 0%,#b9c9d3 100%)"></div>
    <h2 class="abs script h-white" style="left:212px;top:1195px">Hausgemachte<br>Tiernahrung</h2>
    <p class="abs body-text" style="left:212px;top:1249px;width:184px;color:#fff">Lorem ipsum dolor sit amet, consectetur adipiscing elit, sed do eiusmod tempor incididunt ut labore et dolore magna aliqua. Ut enim ad minim veniam, quis nostrud exercitation ullamco laboris nisi ut aliquip ex ea commodo consequat. Duis aute irure dolor in reprehenderit in voluptate velit esse cillum dolore eu fugiat nulla pariatur.</p>
    <h3 class="abs script" style="left:212px;top:1324px;color:#fff;font-size:13px;line-height:14px">Sie können in unserem<br>Online-Shop</h3>
    <ul class="abs tick-list" style="left:212px;top:1355px">
      <li><svg viewBox="0 0 9 7"><path d="M1 3.5 3.5 6 8 1" fill="none" stroke="#fff" stroke-width="1.3"/></svg>Selbsthergestellte Kekse</li>
      <li><svg viewBox="0 0 9 7"><path d="M1 3.5 3.5 6 8 1" fill="none" stroke="#fff" stroke-width="1.3"/></svg>Leckerlies</li>
      <li><svg viewBox="0 0 9 7"><path d="M1 3.5 3.5 6 8 1" fill="none" stroke="#fff" stroke-width="1.3"/></svg>Snacks</li>
      <li><svg viewBox="0 0 9 7"><path d="M1 3.5 3.5 6 8 1" fill="none" stroke="#fff" stroke-width="1.3"/></svg>Pralinen</li>
      <li><svg viewBox="0 0 9 7"><path d="M1 3.5 3.5 6 8 1" fill="none" stroke="#fff" stroke-width="1.3"/></svg>Div. Hausmannskost in Einmachgläsern</li>
    </ul>
    <div class="btn btn-blue" style="left:212px;top:1433px;width:84px;height:15px">Mehr Infos</div>
  </section>

  <section>
    <div class="media" role="img" aria-label="Foto: Katze auf einem gemusterten Kratzmöbel" style="left:200px;top:1526px;width:208px;height:248px;background:linear-gradient(180deg,#ffffff 0%,#e4ddd3 100%)"></div>
    <h2 class="abs script h-orange" style="left:16px;top:1542px">Accessories</h2>
    <p class="abs body-text" style="left:16px;top:1576px;width:180px">Lorem ipsum dolor sit amet, consectetur adipiscing elit, sed do eiusmod tempor incididunt ut labore et dolore magna aliqua. Ut enim ad minim veniam, quis nostrud exercitation ullamco laboris nisi ut aliquip ex ea commodo consequat. Duis aute irure dolor in reprehenderit in voluptate velit esse cillum dolore eu fugiat nulla pariatur.</p>
    <p class="abs body-text" style="left:16px;top:1651px;width:180px">Lorem ipsum dolor sit amet, consectetur adipiscing elit, sed do eiusmod tempor incididunt ut labore et dolore magna aliqua.</p>
    <ul class="abs orange-list" style="left:16px;top:1691px">
      <li>Halsbänder</li>
      <li>Leinen</li>
      <li>Geschirr aus div. natürlichen Materialien</li>
      <li>Lern- und Spielzeug aus Holz und Stoff</li>
      <li>Div. Zubehör für Tiere</li>
    </ul>
    <div class="btn btn-blue" style="left:16px;top:1758px;width:84px;height:15px">Mehr Infos</div>
  </section>

  <section class="abs shop">
    <div class="wave-top" style="top:-8px"></div>
    <h2 class="shop-title script">Online Shop</h2>
    <div class="shop-tabs">ALL ITEMS &nbsp;|&nbsp; FOOD &nbsp;|&nbsp; SNACKS &nbsp;|&nbsp; PRALINEN &nbsp;|&nbsp; ACCESSORIES</div>

    <article class="card" style="left:16px;top:81px"><div class="card-img" role="img" aria-label="Produktfoto Trockenfutter"></div><div class="card-name">PRODUCY NAME GOES HERE</div><p class="card-desc">Lorem ipsum dolor sit amet, consectetur adipiscing elit, sed do eiusmod tempor incididunt ut labore et dolore magna aliqua.</p><div class="card-rule"></div><div class="card-price">€ 10,50</div><div class="card-tax">inkl. 19% MwSt. zzgl.<br><b>Versandkosten</b> &nbsp;|&nbsp; Lieferzeit 2 - 3 tage</div><div class="btn btn-orange">Add to cart</div></article>
    <article class="card" style="left:146px;top:81px"><div class="card-img" role="img" aria-label="Produktfoto Trockenfutter"></div><div class="card-name">PRODUCY NAME GOES HERE</div><p class="card-desc">Lorem ipsum dolor sit amet, consectetur adipiscing elit, sed do eiusmod tempor incididunt ut labore et dolore magna aliqua.</p><div class="card-rule"></div><div class="card-price">€ 10,50</div><div class="card-tax">inkl. 19% MwSt. zzgl.<br><b>Versandkosten</b> &nbsp;|&nbsp; Lieferzeit 2 - 3 tage</div><div class="btn btn-blue">Add to cart</div></article>
    <article class="card" style="left:276px;top:81px"><div class="card-img" role="img" aria-label="Produktfoto Trockenfutter"></div><div class="card-name">PRODUCY NAME GOES HERE</div><p class="card-desc">Lorem ipsum dolor sit amet, consectetur adipiscing elit, sed do eiusmod tempor incididunt ut labore et dolore magna aliqua.</p><div class="card-rule"></div><div class="card-price">€ 10,50</div><div class="card-tax">inkl. 19% MwSt. zzgl.<br><b>Versandkosten</b> &nbsp;|&nbsp; Lieferzeit 2 - 3 tage</div><div class="btn btn-blue">Add to cart</div></article>

    <article class="card" style="left:16px;top:306px"><div class="card-img" role="img" aria-label="Produktfoto Trockenfutter"></div><div class="card-name">PRODUCY NAME GOES HERE</div><p class="card-desc">Lorem ipsum dolor sit amet, consectetur adipiscing elit, sed do eiusmod tempor incididunt ut labore et dolore magna aliqua.</p><div class="card-rule"></div><div class="card-price">€ 10,50</div><div class="card-tax">inkl. 19% MwSt. zzgl.<br><b>Versandkosten</b> &nbsp;|&nbsp; Lieferzeit 2 - 3 tage</div><div class="btn btn-blue">Add to cart</div></article>
    <article class="card" style="left:146px;top:306px"><div class="card-img" role="img" aria-label="Produktfoto Trockenfutter"></div><div class="card-name">PRODUCY NAME GOES HERE</div><p class="card-desc">Lorem ipsum dolor sit amet, consectetur adipiscing elit, sed do eiusmod tempor incididunt ut labore et dolore magna aliqua.</p><div class="card-rule"></div><div class="card-price">€ 10,50</div><div class="card-tax">inkl. 19% MwSt. zzgl.<br><b>Versandkosten</b> &nbsp;|&nbsp; Lieferzeit 2 - 3 tage</div><div class="btn btn-blue">Add to cart</div></article>
    <article class="card" style="left:276px;top:306px"><div class="card-img" role="img" aria-label="Produktfoto Trockenfutter"></div><div class="card-name">PRODUCY NAME GOES HERE</div><p class="card-desc">Lorem ipsum dolor sit amet, consectetur adipiscing elit, sed do eiusmod tempor incididunt ut labore et dolore magna aliqua.</p><div class="card-rule"></div><div class="card-price">€ 10,50</div><div class="card-tax">inkl. 19% MwSt. zzgl.<br><b>Versandkosten</b> &nbsp;|&nbsp; Lieferzeit 2 - 3 tage</div><div class="btn btn-blue">Add to cart</div></article>

    <div class="btn btn-blue" style="left:135px;top:528px;width:137px;height:18px;font-size:6.6px">Go to online shop</div>
  </section>

  <section class="abs newsletter">
    <h2 class="news-title">Newsletter anfordern und 5 Euro Gutschein sichern</h2>
    <p class="news-sub">Angebote &amp; Neuigkeiten direkt per E-Mail! (Abmeldung jederzeit möglich)</p>
    <div class="news-input">Email Address</div>
    <div class="news-btn">JETZT ANMELDEN</div>
  </section>

  <footer class="abs site-footer">
    <div class="footer-brand"><span class="brand-name">Napfglück</span><span class="brand-dot"></span></div>
    <p class="address">Company Address will be here &nbsp;|&nbsp; 00112233 &nbsp;|&nbsp; Country Name will go here<br>Fon (0020) 123 44 567 &nbsp;-&nbsp; Fax (0020) 123 44 567<br><span class="web">www.napfglueck.ch &nbsp;|&nbsp; info@napfglueck.ch</span></p>
    <div class="social"><span></span><span></span><span></span><span></span><span></span></div>
    <h2 class="contact-title script">Kontaktieren Sie uns jetzt</h2>
    <p class="contact-sub">Sie können uns wie folgt erreichen.Wir freuen uns über Ihre Kontakt Anfrage.</p>
    <div class="field active" style="left:16px;top:289px;width:180px">Your Name</div>
    <div class="field" style="left:212px;top:289px;width:180px">Your Email</div>
    <div class="field" style="left:16px;top:318px;width:376px">Subject</div>
    <div class="field" style="left:16px;top:347px;width:376px;height:40px">Your Message</div>
    <div class="abs" style="left:16px;top:415px;width:376px;border-top:1px solid var(--line)"></div>
    <div class="copy-check">Send copy to yourself <i></i></div>
    <div class="btn btn-orange" style="left:288px;top:428px;width:104px;height:18px;font-size:6.8px">Send Message</div>
  </footer>

  <div class="abs bottom-bar">
    <span class="left">© 2017 Napfglück - All Rights reserved</span>
    <span class="right">PRIVACY &nbsp;|&nbsp; IMPRESSUM &nbsp;|&nbsp; AGB &nbsp;|&nbsp; KONTAKT</span>
  </div>
</div>
</body>
</html>
```